The Hidden Roots of Lingering Illness Decoded

Subtitle: At last, uncover what drives your aches, exhaustion, and swelling.

I need an awesome book cover that fits this title.

```html
<!DOCTYPE html>
<html lang="en">
<head>
<meta charset="utf-8">
<title>The Hidden Roots of Lingering Illness Decoded — Book Cover</title>
<link rel="stylesheet" href="https://fonts.googleapis.com/css2?family=Bebas+Neue&family=Montserrat:wght@500;600&display=swap">
<style>
  :root {
    --page: #ffffff;
    --cover-green: #1e6358;
    --title-white: #ffffff;
    --gold-edge: #e8921f;
    --gold-mid: #ffe205;
    --sky-peach: #f6b36a;
    --sky-rose: #e9805e;
    --sky-haze: #d9d3bd;
    --ridge: #5d5a4c;
    --ink: #111111;
  }
  html, body {
    margin: 0;
    padding: 0;
    width: 1200px;
    height: 1200px;
    overflow: hidden;
    background: var(--page);
  }
  .book-cover {
    position: absolute;
    left: 222px;
    top: 31px;
    width: 764px;
    height: 1146px;
    background: var(--cover-green);
  }
  .book-cover svg {
    display: block;
    width: 100%;
    height: 100%;
  }
  .title {
    font-family: "Bebas Neue", "Oswald", sans-serif;
    text-anchor: middle;
  }
  .title-lead {
    font-family: "Montserrat", sans-serif;
    font-weight: 500;
    font-size: 74px;
    fill: var(--title-white);
    text-anchor: middle;
  }
  .title-gold { fill: url(#goldGradient); }
  .title-white { fill: var(--title-white); }
  .subtitle {
    font-family: "Montserrat", sans-serif;
    font-weight: 600;
    font-size: 31px;
    fill: var(--ink);
    text-anchor: middle;
  }
  .author {
    font-family: "Montserrat", sans-serif;
    font-weight: 600;
    font-size: 40px;
    letter-spacing: 12px;
    fill: var(--title-white);
    text-anchor: middle;
  }
</style>
</head>
<body>
  <div class="book-cover">
    <svg viewBox="0 0 900 1350" xmlns="http://www.w3.org/2000/svg" aria-labelledby="cover-title">
      <title id="cover-title">The Hidden Roots of Lingering Illness Decoded</title>
      <defs>
        <linearGradient id="goldGradient" x1="122" y1="0" x2="798" y2="0" gradientUnits="userSpaceOnUse">
          <stop offset="0" stop-color="var(--gold-edge)"/>
          <stop offset="0.55" stop-color="var(--gold-mid)"/>
          <stop offset="1" stop-color="var(--gold-edge)"/>
        </linearGradient>
        <linearGradient id="sunsetSky" x1="0" y1="0" x2="0" y2="1">
          <stop offset="0" stop-color="var(--sky-peach)"/>
          <stop offset="0.35" stop-color="var(--sky-rose)"/>
          <stop offset="0.62" stop-color="#f0b061"/>
          <stop offset="0.8" stop-color="var(--sky-haze)"/>
          <stop offset="1" stop-color="var(--ridge)"/>
        </linearGradient>
        <linearGradient id="glowLine" x1="0" y1="0" x2="1" y2="0">
          <stop offset="0" stop-color="#ffe600" stop-opacity="0"/>
          <stop offset="0.5" stop-color="#fff35a"/>
          <stop offset="1" stop-color="#ffe600" stop-opacity="0"/>
        </linearGradient>
        <filter id="softEdge" x="-10%" y="-10%" width="120%" height="120%">
          <feGaussianBlur stdDeviation="22"/>
        </filter>
      </defs>

      <!-- title block -->
      <g class="title-block">
        <line x1="122" y1="76" x2="338" y2="76" stroke="var(--title-white)" stroke-width="4"/>
        <line x1="583" y1="76" x2="798" y2="76" stroke="var(--title-white)" stroke-width="4"/>
        <text class="title-lead" x="461" y="103">THE</text>

        <text class="title title-gold" x="460" y="233" font-size="157" textLength="676" lengthAdjust="spacingAndGlyphs">HIDDEN ROOTS OF</text>
        <text class="title title-gold" x="460" y="430" font-size="260" textLength="676" lengthAdjust="spacingAndGlyphs">LINGERING</text>
        <text class="title title-white" x="460" y="610" font-size="231" textLength="676" lengthAdjust="spacingAndGlyphs">ILLNESS</text>
        <text class="title title-white" x="460" y="781" font-size="219" textLength="676" lengthAdjust="spacingAndGlyphs">DECODED</text>
      </g>

      <!-- sunset photo area -->
      <rect class="photo-area" x="40" y="820" width="820" height="420" fill="url(#sunsetSky)" filter="url(#softEdge)"
            role="img" aria-label="Photo of a person sitting on a hilltop facing a golden sunset above the clouds"/>

      <!-- subtitle -->
      <rect x="270" y="821" width="360" height="3" fill="url(#glowLine)"/>
      <text class="subtitle" x="463" y="866">At last, uncover what drives your aches,</text>
      <text class="subtitle" x="463" y="909">exhaustion, and swelling.</text>
      <rect x="270" y="933" width="360" height="3" fill="url(#glowLine)"/>

      <!-- author -->
      <text class="author" x="456" y="1319">AUTHOR NAME</text>
    </svg>
  </div>
</body>
</html>
```